Redesign This Psychology Website

We would like a slight redesign of this successful psychology (relationship counselling) website:

www.TheWillowNook.com.au

We are updating the website, and we'd like a slight refresh of the design and style.

Please keep to very similar colours, and use the same logo. We're looking for around 10 page templates, however the main one is the home page.

Keep in mind, this website already converts quite well, so we want a new, fresh design in keeping with this one. Please don't bother designing something too extremely different.

thanks :)

Target Market(s)

couples who are looking for relationship counselling. Men and women, 25 - 70, across Australia

Industry/Entity Type

Psychology

Number of Pages Required

5+ page

Font styles to use
Sans Serif

Colors
87cfc6
b7a5cd
ec1f27
ffffff
cee9f5

Requirements
Must have
• a similar look to the current design, just looking for a slight refresh.
• Search bar
• Areas for lots of photos
• same logo
• lots of content areas
Nice to have
• great content areas, where we can display a lot of content and our areas.
Should not have
• no colors like orange, etc.
• should not have a totally different feel.

```html
<!DOCTYPE html>
<html lang="en">
<head>
<meta charset="utf-8">
<title>The Willow Nook – Relationship Counselling</title>
<link href="https://fonts.googleapis.com/css2?family=Montserrat:ital,wght@0,400;0,500;0,600;0,700;1,500&display=swap" rel="stylesheet">
<style>
:root{
  --teal:#17858f;
  --teal-deep:#0f6d76;
  --mint:#87cfc6;
  --mint-soft:#e4f4f2;
  --lilac:#b7a5cd;
  --lilac-soft:#efeaf5;
  --red:#ec1f27;
  --ice:#cee9f5;
  --ice-soft:#eef7fb;
  --ink:#2f3a3d;
  --body:#4a5457;
  --muted:#7a8487;
  --white:#fff;
  --line:#e2e8ea;
  --topbar:#1f3134;
}
*{box-sizing:border-box;margin:0;padding:0}
html,body{width:1200px;height:3291px;overflow:hidden}
body{font-family:"Montserrat",Arial,sans-serif;color:var(--ink);background:var(--white);font-size:12px;line-height:1.55}
a{color:inherit;text-decoration:none}
.wrap{width:1000px;margin:0 auto;position:relative}
.heading{font-weight:700;color:var(--red);letter-spacing:-.3px;line-height:1.2}
.heading::after{content:"";display:block;width:48px;height:4px;border-radius:2px;background:var(--mint);margin-top:10px}
.heading.center{text-align:center}
.heading.center::after{margin:10px auto 0}
.btn{display:inline-flex;align-items:center;justify-content:center;font-weight:600;color:#fff;background:var(--red);font-size:12px;border-radius:999px;white-space:nowrap}
.btn.teal{background:var(--teal)}

/* top bar */
.topbar{height:26px;background:var(--topbar);color:#cfdcde;font-size:9.5px;letter-spacing:.4px}
.topbar .wrap{display:flex;justify-content:space-between;align-items:center;height:26px}
.topbar nav a{margin-right:18px}
.topbar .shop a{margin-left:16px;color:#fff;font-weight:600}

/* header */
.header{height:68px}
.header .wrap{display:flex;justify-content:space-between;align-items:center;height:68px}
.brand{display:flex;align-items:center;gap:10px}
.brand-dot{width:30px;height:30px;border-radius:50%;background:var(--teal)}
.brand-name{font-size:21px;font-weight:600;color:var(--teal);line-height:1;display:block}
.brand-tag{font-size:9px;color:var(--muted);display:block;margin-top:4px}
.contact{display:flex;align-items:center;gap:22px}
.contact .phone{text-align:right}
.contact small{font-size:10px;font-weight:600;display:block;line-height:1.1;color:var(--muted)}
.contact strong{font-size:19px;color:var(--teal);font-weight:600;line-height:1.2;display:block}
.search{display:flex;align-items:center;border:1px solid var(--line);border-radius:999px;height:30px;width:200px;padding:0 4px 0 12px;background:var(--ice-soft)}
.search input{flex:1;border:0;background:transparent;height:28px;font:inherit;font-size:11px}
.search button{width:24px;height:24px;border:0;border-radius:50%;background:var(--teal);display:flex;align-items:center;justify-content:center}

/* main nav */
.mainnav{height:33px;border-top:1px solid var(--line);border-bottom:1px solid var(--line)}
.mainnav .wrap{display:flex;height:31px;align-items:center;justify-content:space-between}
.mainnav a{font-size:11px;font-weight:600;padding:0 8px;height:23px;display:flex;align-items:center;color:var(--ink);white-space:nowrap;border-radius:999px}
.mainnav a.active{background:var(--teal);color:#fff;padding:0 14px}

/* hero */
.hero{height:391px;position:relative;overflow:hidden}
.hero-scene{position:absolute;inset:0;background:
  radial-gradient(ellipse at 60% 38%,rgba(236,31,120,.45) 0%,rgba(236,31,120,0) 36%),
  radial-gradient(ellipse at 86% 42%,rgba(250,232,218,.95) 0%,rgba(250,232,218,0) 22%),
  linear-gradient(180deg,#8cc8ea 0%,var(--ice) 60%,#f2f9fc 100%)}
.hero-fade{position:absolute;left:0;right:0;bottom:0;height:60px;background:linear-gradient(180deg,rgba(255,255,255,0),#fff)}
.hero-video{position:absolute;left:100px;top:58px;width:470px;height:268px;border-radius:14px;overflow:hidden;background:linear-gradient(90deg,#6f98a8 0%,#c4d6dc 55%,#e3cfb8 100%);box-shadow:0 12px 30px rgba(15,109,118,.25);border:5px solid #fff}
.hero-video .bar{position:absolute;left:0;right:0;bottom:0;height:26px;background:rgba(15,49,52,.6);display:flex;align-items:center;padding-left:12px}

/* service cards */
.services{height:425px;padding-top:38px}
.services .wrap{display:flex;justify-content:space-between}
.card{width:235px;height:350px;border-radius:14px;background:#fff;border:1px solid var(--line);border-top:4px solid var(--mint);box-shadow:0 6px 18px rgba(23,133,143,.08);padding:10px 12px 0;display:flex;flex-direction:column}
.card h3{font-size:11px;font-weight:700;color:var(--red);text-align:center;line-height:1.3;height:32px;display:flex;align-items:center;justify-content:center;text-transform:uppercase;letter-spacing:.6px}
.card .photo{height:128px;border-radius:10px;margin:4px 0 10px}
.card h4{font-size:13px;font-weight:600;color:var(--teal);margin-bottom:3px}
.card p{font-size:10px;color:var(--body);line-height:1.5}
.card .link{font-size:10.5px;font-weight:600;color:var(--teal);margin-top:7px;line-height:1.35}
.card .btn{width:112px;height:32px;margin-top:auto;margin-bottom:14px;align-self:flex-start}

/* specialise */
.special{height:384px;position:relative;background:linear-gradient(90deg,var(--ice-soft) 0%,var(--ice) 100%)}
.special .text{position:absolute;left:100px;top:38px;width:490px}
.special .heading{font-size:24px;margin-bottom:16px}
.special p{font-size:11.5px;color:var(--body);margin-bottom:12px}
.special p a{color:var(--teal);font-weight:600}
.special .photo{position:absolute;left:640px;top:30px;right:0;bottom:30px;border-radius:24px 0 0 24px;background:linear-gradient(120deg,#cfe2ee 0%,#b7ccd9 25%,#d7b59c 60%,#9c7361 100%)}

/* psychologists */
.team{height:621px;position:relative}
.team .heading{font-size:26px;padding-top:26px}
.team .intro{text-align:center;font-size:11.5px;color:var(--body);margin-top:14px;line-height:1.6}
.team .intro p{margin-bottom:8px}
.team .intro b{color:var(--teal);font-weight:600}
.team .intro .accent{color:var(--teal);font-weight:600;margin-bottom:0}
.team .lower{position:absolute;left:0;right:0;top:232px;height:360px}
.team h5{font-size:12.5px;font-weight:700;color:var(--teal);margin-bottom:8px}
.issues{list-style:none;columns:2;column-gap:30px;width:470px;background:var(--mint-soft);border-radius:14px;padding:16px 20px}
.issues li{font-size:11px;color:var(--teal-deep);height:22px;display:flex;align-items:center;gap:8px;break-inside:avoid}
.issues li::before{content:"";flex:none;width:8px;height:8px;border-radius:50%;background:var(--lilac)}
.team .big{position:absolute;right:0;top:0;width:320px;height:350px;border-radius:16px;background:linear-gradient(150deg,#f3d08a 0%,#c6783c 45%,#5a2f1f 100%);border:5px solid #fff;box-shadow:0 10px 26px rgba(0,0,0,.14)}
.team .small{position:absolute;right:280px;top:110px;width:200px;height:240px;border-radius:16px;background:linear-gradient(160deg,#f6efdc 0%,#d9c8a4 50%,#b9a07c 100%);border:5px solid #fff;box-shadow:0 10px 26px rgba(0,0,0,.14)}

/* expect */
.expect{height:378px;position:relative;background:linear-gradient(180deg,var(--lilac-soft) 0%,#f4eee9 60%,#efe2d6 100%)}
.expect .heading{font-size:26px;padding-top:26px}
.expect .video{position:absolute;left:100px;top:96px;width:560px;height:250px;border-radius:14px;background:linear-gradient(90deg,#c9cfd4 0%,#eef0f1 50%,#bfc6cc 100%);border:5px solid #fff}
.finder{position:absolute;left:680px;top:96px;width:420px;height:250px;border-radius:14px;background:linear-gradient(160deg,var(--teal) 0%,var(--teal-deep) 100%);padding:22px 22px;color:#fff}
.finder h3{font-size:19px;font-weight:700;line-height:1.1;margin-bottom:14px}
.finder label{font-size:10px;display:block;margin-bottom:4px;color:var(--mint)}
.finder .select{height:32px;border-radius:8px;background:#fff;color:#444;font-size:11px;display:flex;align-items:center;justify-content:space-between;padding:0 10px;margin-bottom:12px}
.finder .row{display:flex;gap:14px}
.finder .row div{flex:1}
.finder .field{height:32px;border-radius:8px;background:#fff}
.finder .btn{width:140px;height:32px;margin:16px auto 0;display:flex}

/* approach */
.approach{height:307px;position:relative}
.approach .text{position:absolute;left:100px;top:34px;width:640px}
.approach .heading{font-size:24px;margin-bottom:12px}
.approach p{font-size:11.5px;color:var(--body);margin-bottom:10px}
.approach p a{color:var(--teal);font-weight:600}
.approach .actions{display:flex;gap:14px;margin-top:14px}
.approach .btn{height:42px;font-size:12.5px;padding:0 28px}
.approach .circle{position:absolute;left:848px;top:-30px;width:230px;height:230px;border-radius:50%;border:6px solid #fff;box-shadow:0 10px 26px rgba(0,0,0,.16);background:radial-gradient(circle at 50% 40%,#f3dcc6 0%,#d8b697 50%,#9bb6c8 100%)}
.approach .ring{position:absolute;left:834px;top:-44px;width:258px;height:258px;border-radius:50%;border:2px solid var(--lilac)}

/* blog */
.blog{height:395px;background:var(--ice-soft)}
.blog .heading{font-size:26px;padding-top:22px;margin-bottom:16px}
.blog .wrap{display:flex;justify-content:space-between}
.post{width:320px;height:290px;border-radius:14px;background:#fff;border:1px solid var(--line);box-shadow:0 6px 18px rgba(23,133,143,.08);padding:8px;display:flex;flex-direction:column}
.post .photo{height:150px;border-radius:10px}
.post h4{font-size:12px;font-weight:700;color:var(--teal);margin:10px 6px 4px;line-height:1.3}
.post p{font-size:10px;color:var(--muted);margin:0 6px;line-height:1.5;height:45px;overflow:hidden}
.post .meta{margin:auto 6px 4px;border-top:1px solid var(--line);padding-top:7px;display:flex;justify-content:space-between;font-size:10px;color:var(--muted)}
.post .meta span:last-child{display:flex;gap:6px;align-items:center}

/* quote band */
.quote-area{height:208px;padding-top:11px;background:linear-gradient(180deg,var(--ice-soft) 0%,#fff 100%)}
.quote{height:197px;border-radius:18px;background:linear-gradient(120deg,var(--teal-deep) 0%,var(--teal) 70%,#2a9aa1 100%);position:relative;color:#fff;overflow:hidden}
.quote::before{content:"";position:absolute;right:-60px;top:-80px;width:240px;height:240px;border-radius:50%;background:rgba(135,207,198,.18)}
.quote .avatar{position:absolute;left:24px;top:22px;width:152px;height:152px;border-radius:50%;border:5px solid #fff;background:radial-gradient(circle at 50% 45%,#d6b08a 0%,#9fc7d2 70%)}
.quote blockquote{position:absolute;left:200px;top:24px;width:770px;font-size:19px;font-weight:500;font-style:italic;line-height:1.25}
.quote .sign{position:absolute;left:200px;top:82px;font-size:10px;line-height:1.5;color:#e3f4f2}
.quote .call{position:absolute;right:28px;bottom:22px;font-size:10px;line-height:1.2;color:var(--mint);font-weight:600}
.quote .call strong{display:block;font-size:20px;font-weight:600;color:#fff}

/* footer */
.footer{height:55px;border-top:3px solid var(--mint);background:#f3f6f7;text-align:center;font-size:10.5px;color:var(--body);padding-top:8px;line-height:1.8}
</style>
</head>
<body>

<div class="topbar">
  <div class="wrap">
    <nav><a href="#">JOIN OUR ASSOCIATE PROGRAM</a><a href="#">MARRIAGE COUNSELLING</a><a href="#">RELATIONSHIP COUNSELLING</a></nav>
    <div class="shop"><a href="#">Shop</a><a href="#">Cart</a></div>
  </div>
</div>

<header class="header">
  <div class="wrap">
    <a class="brand" href="#">
      <span class="brand-dot"></span>
      <span><span class="brand-name">The Willow Nook</span><span class="brand-tag">helping you create loving relationships</span></span>
    </a>
    <div class="contact">
      <form class="search">
        <input type="text" aria-label="Search">
        <button type="button" aria-label="Search">
          <svg width="11" height="11" viewBox="0 0 12 12"><circle cx="5" cy="5" r="3.6" fill="none" stroke="#fff" stroke-width="1.6"/><line x1="7.7" y1="7.7" x2="11" y2="11" stroke="#fff" stroke-width="1.8"/></svg>
        </button>
      </form>
      <div class="phone">
        <small>Call Us On</small>
        <strong>1300 555 019</strong>
      </div>
    </div>
  </div>
</header>

<nav class="mainnav">
  <div class="wrap">
    <a class="active" href="#">Home</a><a href="#">About</a><a href="#">Counselling Types</a><a href="#">Relationship Counselling Locations</a><a href="#">Sex Therapy Locations</a><a href="#">Quizzes</a><a href="#">F.A.Q.'s</a><a href="#">Contact</a><a href="#">Resources</a><a href="#">Blog</a>
  </div>
</nav>

<section class="hero">
  <div class="hero-scene" role="img" aria-label="Woman on a beach holding a flowing pink scarf under a bright blue sky"></div>
  <div class="hero-fade"></div>
  <div class="hero-video" role="img" aria-label="Welcome video with the centre's director">
    <div class="bar"><svg width="10" height="11" viewBox="0 0 10 11"><path d="M0 0L10 5.5L0 11Z" fill="#fff"/></svg></div>
  </div>
</section>

<section class="services">
  <div class="wrap">
    <article class="card">
      <h3>Relationship Counselling</h3>
      <div class="photo" role="img" aria-label="Smiling couple embracing" style="background:linear-gradient(135deg,#f1e3c8,#c49a72)"></div>
      <h4>Do you need help with:</h4>
      <p>Communication, Recovering from an affair, Loss of intimacy &amp; love, Power battles, Feeling like friends, not lovers</p>
      <a class="link" href="#">Take our Relationship Quiz<br>Pre-marriage</a>
      <a class="btn" href="#">More</a>
    </article>
    <article class="card">
      <h3>Sex Therapy Counselling</h3>
      <div class="photo" role="img" aria-label="Couple resting together in bed" style="background:linear-gradient(135deg,#f4ede4,#cdb59d)"></div>
      <h4>Do you need help with:</h4>
      <p>Low libido, Erectile difficulties, Premature ejaculation, Differing libidos, Porn addiction, Keeping sex</p>
      <a class="link" href="#">Take our Relationship</a>
      <a class="btn" href="#">More</a>
    </article>
    <article class="card">
      <h3>Anger Management Counselling</h3>
      <div class="photo" role="img" aria-label="Tense couple arguing at home" style="background:linear-gradient(135deg,#e9dccb,#8e6a4c)"></div>
      <h4>Do you need help with:</h4>
      <p>Communication, Recovering from an affair, Loss of intimacy &amp; love, Power battles, Feeling like friends, not lovers</p>
      <a class="link" href="#">Take our Anger Test</a>
      <a class="btn" href="#">More</a>
    </article>
    <article class="card">
      <h3>Narcissism Counselling</h3>
      <div class="photo" role="img" aria-label="Upset woman sitting on a sofa" style="background:linear-gradient(135deg,#c9d6e2,#7f95a8)"></div>
      <h4>Do you need help with:</h4>
      <p>Communication, Recovering from an affair, Loss of intimacy &amp; love, Power battles, Feeling like friends, not lovers</p>
      <a class="link" href="#">Check your Narcissism Profile</a>
      <a class="btn" href="#">More</a>
    </article>
  </div>
</section>

<section class="special">
  <div class="text">
    <h2 class="heading">We Specialise in Relationship &amp; Marriage Counselling</h2>
    <p>At The Willow Nook, we are a group of PSYCHOLOGISTS, Australia wide who are passionate about relationships and helping you with yours.</p>
    <p>Our vision is to provide the most highly regarded and comprehensive <a href="#">marriage counselling</a> and relationship counselling, and sex therapy in Australia, at reasonable and affordable rates.</p>
    <p>When we are experiencing relationship and marriage problems, there can be a lot of pain and confusion, and it can often be difficult to cope with the other areas of our lives when we are struggling with problems with our partner.</p>
    <p>We are not taught about relationships and how to have a good one in our schools, so most of us are doing the best we know how, but lack the knowledge on how to create a better relationship.</p>
  </div>
  <div class="photo" role="img" aria-label="Happy couple sharing ice cream outdoors"></div>
</section>

<section class="team">
  <h2 class="heading center">Our Willow Nook Relationship Psychologists</h2>
  <div class="intro wrap">
    <p>Our team of 75 hand chosen <b>Registered Psychologists</b> in 81 locations Australia wide, are individually selected for their knowledge, experience, compassion, and unbiased approach to marriage counselling and sexual therapy.</p>
    <p>In addition all our Psychologists take part in our Initial Relationship Counselling Methodologies Training and yearly in house conferences, ensuring you are in safe and experienced hands.</p>
    <p class="accent">As we are Psychologists, you may be eligible for Medicare &amp; Private Health Insurance Rebates.</p>
    <p>We are highly experienced and can help you with all kinds of relationship difficulties.</p>
  </div>
  <div class="wrap lower">
    <h5>Here are some of the common ones:</h5>
    <ul class="issues">
      <li>Affairs</li><li>Controlling behaviour</li><li>Verbal abuse</li><li>Imbalance of power</li><li>Lack of intimacy</li><li>Poor communication</li><li>Loss of love</li><li>Relationship neglect</li><li>Sexual problems</li><li>Problems from childhood</li><li>Problems with parenting</li><li>Step children and in-laws</li><li>All forms of family problems</li><li>Anger management problems</li><li>Porn addiction problems</li><li>Pre-marriage programs</li><li>Narcissism problems</li>
    </ul>
    <div class="big" role="img" aria-label="Couple embracing at sunset"></div>
    <div class="small" role="img" aria-label="Couple hugging in soft light"></div>
  </div>
</section>

<section class="expect">
  <h2 class="heading center">What To Expect From Counselling</h2>
  <div class="video" role="img" aria-label="Video of a couple in a counselling session"></div>
  <form class="finder">
    <h3>Find Our Psychologist Near You</h3>
    <label>Type of Counselling</label>
    <div class="select">Select
      <svg width="9" height="6" viewBox="0 0 9 6"><path d="M0 0H9L4.5 6Z" fill="#333"/></svg>
    </div>
    <div class="row">
      <div><label>Location</label><div class="field"></div></div>
      <div><label>Postcode</label><div class="field"></div></div>
    </div>
    <a class="btn" href="#">Search</a>
  </form>
</section>

<section class="approach">
  <div class="text">
    <h2 class="heading">Our Relationship Counselling Approach</h2>
    <p>It is an important part of our policy to take a <a href="#">very positive approach</a> to our relationship counselling.</p>
    <p>We feel it is important to really understand the problems and perspectives of each of you, and at the same time, we find that most couples are looking to find a positive action plan and way through their problems to make changes which have a positive impact and a real sense of hope for their relationship.</p>
    <p>Read more about our approach to counselling in our <a href="#">relationship counselling sessions, and frequently asked questions about the relationship and marriage counselling process.</a></p>
    <div class="actions">
      <a class="btn teal" href="#">Take our Willow Nook Relationship Assessment</a>
      <a class="btn" href="#">About Us</a>
    </div>
  </div>
  <div class="ring"></div>
  <div class="circle" role="img" aria-label="Smiling couple close together"></div>
</section>

<section class="blog">
  <h2 class="heading center">Our Blog</h2>
  <div class="wrap">
    <article class="post">
      <div class="photo" role="img" aria-label="Couple holding hands across a table" style="background:linear-gradient(135deg,#e7d2bd,#a86a4a)"></div>
      <h4>What Are You Like In a Relationship?</h4>
      <p>Successful couples counselling requires at least one person to make significant behavioural changes that their partner recognises as beneficial. However, the relationships that</p>
      <div class="meta"><span>October 5, 2016</span><span><svg width="10" height="9" viewBox="0 0 10 9"><path d="M0 0H10V6H4L1 9V6H0Z" fill="#7a8487"/></svg><svg width="10" height="9" viewBox="0 0 10 9"><path d="M5 9L0.6 4.4A2.4 2.4 0 0 1 5 1.6A2.4 2.4 0 0 1 9.4 4.4Z" fill="#ec1f27"/></svg></span></div>
    </article>
    <article class="post">
      <div class="photo" role="img" aria-label="Hand raised in a stop gesture" style="background:linear-gradient(135deg,#d9d2cc,#5a4a44)"></div>
      <h4>Are You Living With a Steamroller?</h4>
      <p>Some partners push through every discussion without pausing to listen. Over time this leaves the other person feeling unheard, worn down and unsure of how to speak up again.</p>
      <div class="meta"><span>October 5, 2016</span><span><svg width="10" height="9" viewBox="0 0 10 9"><path d="M0 0H10V6H4L1 9V6H0Z" fill="#7a8487"/></svg><svg width="10" height="9" viewBox="0 0 10 9"><path d="M5 9L0.6 4.4A2.4 2.4 0 0 1 5 1.6A2.4 2.4 0 0 1 9.4 4.4Z" fill="#ec1f27"/></svg></span></div>
    </article>
    <article class="post">
      <div class="photo" role="img" aria-label="Woman looking worried beside her partner" style="background:linear-gradient(135deg,#e2e4e6,#8e9399)"></div>
      <h4>Why am I with a Narcissist?</h4>
      <p>Many people find themselves drawn to charming partners who later seem cold and self focused. Understanding this pattern is the first step towards healthier choices.</p>
      <div class="meta"><span>October 5, 2016</span><span><svg width="10" height="9" viewBox="0 0 10 9"><path d="M0 0H10V6H4L1 9V6H0Z" fill="#7a8487"/></svg><svg width="10" height="9" viewBox="0 0 10 9"><path d="M5 9L0.6 4.4A2.4 2.4 0 0 1 5 1.6A2.4 2.4 0 0 1 9.4 4.4Z" fill="#ec1f27"/></svg></span></div>
    </article>
  </div>
</section>

<div class="quote-area">
  <section class="quote wrap">
    <div class="avatar" role="img" aria-label="Portrait of the centre's director"></div>
    <blockquote>“At the end of our life, what matters most is how well did we love”</blockquote>
    <div class="sign">
      Maren Ashby Director – Psychologist<br>
      You can read more about relationship counselling here<br>
      Warmly,<br>
      Maren Ashby<br>
      Director – Psychologist<br>
      Grad Dip Psych, Post Grad Dip Psych, B Ed, Dip Teach, MAPS
    </div>
    <div class="call">CALL US ON<strong>1300 555 019</strong></div>
  </section>
</div>

<footer class="footer">
  © Copyright The Willow Nook 2017 Visit us on Socials<br>
  Privacy Policy Terms &amp; Conditions Site Map Associate Psychologists Program Contact Us
</footer>

</body>
</html>
```